Photovoltaik Anbieter sucht Transporterbeschriftung
Zielgruppe
Kalvberg Planungs- und Betriebs GmbH plant und installiert Photovoltaikanlagen für industrielle Großanlagen. Im Landkreis Lüneburg sind wir der größte Anbieter und bauen und betreuen vornehmlich große Projekte. Unser Anspruch ist es dabei, professionell und perfektionistisch zu arbeiten, um die höchste Qualität gewährleisten zu können. Unsere Zielgruppe sind große industrielle Unternehmen, Besitzer von Freiflächen, Energieversorger und landwirtschaftliche Kunden.
Aufgabenstellung
Design:
...technisch und kühl, professionell, auf Industrie zugeschnitten
...inklusive bestehendem Logo
...Farben aus Logo: gelb, grau
...entweder mit grafischen Elementen oder mit Bildern von technischen Details, Single Line Diagramm, Trafo/Stromspeicher Icon usw.
...Eye-Catcher, hebt sich im besten Fall von lokaler Konkurrenz ab, fällt auf
Bitte nicht das Design von der Website beachten! Diese ist veraltet und wird derzeit bearbeitet

```html
<!DOCTYPE html>
<html lang="de">
<head>
<meta charset="utf-8">
<title>Kalvberg – Transporterbeschriftung</title>
<link href="https://fonts.googleapis.com/css2?family=Archivo:wght@400;800;900&display=swap" rel="stylesheet">
<style>
  :root {
    --white: #ffffff;
    --yellow: #f0c04c;
    --grey: #6e6e70;
    --grey-dark: #3a3a3c;
    --grey-light: #8c8c8e;
    --text-grey: #707072;
  }
  html, body {
    margin: 0;
    padding: 0;
    overflow: hidden;
    background: var(--white);
  }
  .wrap-side {
    position: relative;
    width: 1200px;
    height: 600px;
    overflow: hidden;
    background: var(--white);
    font-family: "Archivo", sans-serif;
  }
  .wrap-side__bands {
    position: absolute;
    inset: 0;
  }
  .brand {
    position: absolute;
    left: 541px;
    top: 116px;
    width: 490px;
    height: 134px;
    display: flex;
    align-items: center;
    justify-content: center;
  }
  .brand__name {
    font-weight: 900;
    font-size: 80px;
    letter-spacing: 1px;
    color: var(--text-grey);
    line-height: 1;
  }
  .phone {
    position: absolute;
    left: 168px;
    top: 305px;
    display: flex;
    align-items: center;
    gap: 4px;
    font-weight: 800;
    font-size: 28px;
    letter-spacing: 1px;
    color: var(--text-grey);
  }
  .phone svg { width: 21px; height: 21px; }
  .slogan {
    position: absolute;
    left: 512px;
    top: 333px;
    margin: 0;
    font-weight: 800;
    font-size: 19px;
    line-height: 25px;
    letter-spacing: 0.5px;
    color: var(--white);
  }
  .web {
    position: absolute;
    left: 474px;
    width: 320px;
    top: 443px;
    text-align: center;
    font-weight: 400;
    font-size: 20px;
    letter-spacing: 0.5px;
    color: var(--yellow);
  }
</style>
</head>
<body>
<main class="wrap-side">
  <svg class="wrap-side__bands" width="1200" height="600" viewBox="0 0 1200 600" aria-hidden="true">
    <path class="band-grey" fill="#6e6e70" d="M290 391 C540 324 820 300 1200 298 L1200 391 Z"/>
    <path class="band-yellow" fill="#f0c04c" d="M276 391 C520 304 800 274 1200 268 L1200 299 C820 300 540 324 290 391 Z"/>
    <rect class="band-dark" x="0" y="390" width="1200" height="41" fill="#3a3a3c"/>
    <rect class="band-light" x="0" y="431" width="1200" height="51" fill="#8c8c8e"/>
  </svg>

  <div class="brand">
    <span class="brand__name">KALVBERG</span>
  </div>

  <div class="phone">
    <svg viewBox="0 0 24 24" aria-hidden="true">
      <rect x="0" y="0" width="24" height="24" rx="5" fill="#707072"/>
      <path fill="#ffffff" d="M8 5c-1.2 0-2.2 1.4-1.8 3.4.8 4.4 4.6 9 8.8 10.4 1.8.6 3-.2 3.3-1.3l.3-1.2-3.2-1.6-1.3 1.4c-2-1-3.8-3.2-4.6-5.3l1.5-1.1L9.7 5.3z"/>
    </svg>
    <span>04131 / 5290</span>
  </div>

  <p class="slogan">Nie wieder<br>Strompreis-Erhöhung!</p>

  <div class="web">WWW.KALVBERG.DE</div>
</main>
</body>
</html>
```